Lagoonworks Solutions

I run an aquarium service business covering all aspects of large scale saltwater aquariums. Design, installation, and service. My main customer base is corporations in Manhattan, but I also deal with smaller home or business aquariums in the tri-state area. I work with cutting edge equipment and service techniques and need to convey that.

Industry/Entity Type

Business

Contact Information for Business Card

LAGOONWORKS SOLUTIONS LLC
Jonathan R. Delvoy
Owner
Main 415-555-0182
Cell 415-555-0267
Service.LagoonSolutions@mailbeam.net

```html
<!DOCTYPE html>
<html lang="en">
<head>
<meta charset="utf-8">
<title>Lagoonworks Solutions – Business Card</title>
<link rel="stylesheet" href="https://fonts.googleapis.com/css2?family=Italiana&family=Crimson+Text&display=swap">
<style>
  :root {
    --page-bg: #3a3836;
    --card-top: #f5f8fb;
    --card-mid: #c6d7e8;
    --card-low: #8eaad0;
    --card-bottom: #6a86bb;
    --side-strip: #d3dce3;
    --info-band: rgba(118, 158, 208, 0.55);
    --ink: #56606c;
    --ink-title: #5f6670;
    --art-light: #c9d2de;
    --art-dark: #5e6b85;
  }
  * { box-sizing: border-box; margin: 0; padding: 0; }
  html, body {
    width: 1200px;
    height: 1200px;
    overflow: hidden;
  }
  body {
    background: var(--page-bg);
    display: flex;
    align-items: center;
    justify-content: center;
  }
  .business-card {
    position: relative;
    width: 1000px;
    height: 572px;
    overflow: hidden;
    background: linear-gradient(180deg,
      var(--card-top) 0%,
      var(--card-top) 28%,
      var(--card-mid) 50%,
      var(--card-low) 78%,
      var(--card-bottom) 100%);
  }
  .side-strip {
    position: absolute;
    left: 0; top: 0;
    width: 46px; height: 100%;
    background: var(--side-strip);
  }
  .emblem-art {
    position: absolute;
    left: 90px; top: 80px;
    width: 190px; height: 430px;
    border-radius: 40px;
    background: radial-gradient(ellipse at 50% 45%, var(--art-light) 0%, var(--art-dark) 70%, rgba(94,107,133,0) 100%);
    opacity: 0.85;
  }
  .info-band {
    position: absolute;
    left: 372px; top: 196px;
    width: 628px; height: 250px;
    background: var(--info-band);
  }
  .company-name {
    position: absolute;
    left: 385px; top: 124px;
    width: 590px;
    font-family: "Italiana", serif;
    font-size: 52px;
    font-weight: 400;
    letter-spacing: 0;
    color: var(--ink-title);
    white-space: nowrap;
  }
  .contact {
    position: absolute;
    left: 392px; top: 216px;
    width: 590px;
    font-family: "Crimson Text", serif;
    color: var(--ink);
    line-height: 1.15;
  }
  .contact .person { font-size: 38px; }
  .contact .role { font-size: 26px; margin-left: 10px; }
  .contact .phone { font-size: 32px; }
  .contact .email { font-size: 26px; margin-top: 8px; white-space: nowrap; }
</style>
</head>
<body>
  <div class="business-card">
    <div class="side-strip"></div>
    <div class="emblem-art" role="img" aria-label="Mechanical seahorse illustration surrounded by water droplets"></div>
    <div class="info-band"></div>
    <h1 class="company-name">Lagoonworks Solutions</h1>
    <div class="contact">
      <p class="person">Jonathan R. Delvoy<span class="role">Owner</span></p>
      <p class="phone">Main: 415-555-0182</p>
      <p class="phone">Cell: 415-555-0267</p>
      <p class="email">Service.LagoonSolutions@mailbeam.net</p>
    </div>
  </div>
</body>
</html>
```